Business Card Design - Local Discount Club

Looking for a fun business card for a local discount club. One side should be the logo only and the other should be have :

Name
Title
Phone, Email
Website

```html
<!DOCTYPE html>
<html lang="en">
<head>
<meta charset="utf-8">
<title>Shoreline Perks Club – Business Cards</title>
<link rel="stylesheet" href="https://fonts.googleapis.com/css2?family=Open+Sans:wght@400;600;800&display=swap">
<style>
  :root {
    --page-bg: #ece9e4;
    --club-blue: #3c63c4;
    --club-blue-deep: #2f51a8;
    --sky: #5ec3e4;
    --mint: #a9d9a0;
    --paper: #f4f5f7;
    --white: #ffffff;
    --ink-shadow: rgba(20, 30, 60, 0.22);
  }
  * { box-sizing: border-box; margin: 0; padding: 0; }
  html, body {
    width: 1200px;
    height: 1023px;
    overflow: hidden;
    background: var(--page-bg);
    font-family: "Open Sans", Arial, sans-serif;
  }
  .canvas {
    position: relative;
    width: 1200px;
    height: 1023px;
  }
  .card {
    position: absolute;
    width: 600px;
    height: 343px;
    border-radius: 6px;
    overflow: hidden;
    box-shadow: 0 10px 26px var(--ink-shadow);
  }

  /* Front side: logo only */
  .card--front {
    left: 90px;
    top: 110px;
    background: linear-gradient(135deg, #4a72d0 0%, var(--club-blue) 55%, var(--club-blue-deep) 100%);
    display: flex;
    align-items: center;
    justify-content: center;
    gap: 18px;
  }
  .brand-name {
    font-weight: 800;
    letter-spacing: 0.5px;
    line-height: 1.05;
    text-transform: uppercase;
  }
  .card--front .brand-name {
    color: var(--white);
    font-size: 46px;
    text-align: left;
  }
  .brand-dot {
    width: 30px;
    height: 30px;
    border-radius: 50%;
    background: var(--sky);
    flex: none;
  }

  /* Back side: contact details */
  .card--back {
    left: 510px;
    top: 570px;
    background: var(--club-blue);
  }
  .back-top {
    position: absolute;
    left: 0; top: 0;
    width: 100%;
    height: 128px;
    background: linear-gradient(180deg, var(--white) 0%, var(--paper) 100%);
  }
  .back-brand {
    position: absolute;
    left: 34px;
    top: 34px;
    display: flex;
    align-items: center;
    gap: 14px;
  }
  .back-brand .brand-name {
    color: var(--club-blue);
    font-size: 30px;
  }
  .back-brand .brand-dot {
    width: 20px;
    height: 20px;
  }
  .contact {
    position: absolute;
    left: 34px;
    top: 152px;
    right: 34px;
    color: var(--white);
  }
  .contact__name {
    font-size: 22px;
    font-weight: 800;
    letter-spacing: 0.5px;
  }
  .contact__title {
    font-size: 15px;
    color: var(--mint);
    margin-bottom: 14px;
  }
  .contact__list {
    list-style: none;
    display: grid;
    grid-template-columns: 1fr 1fr;
    row-gap: 9px;
    column-gap: 20px;
    font-size: 13.5px;
  }
  .contact__item {
    display: flex;
    align-items: flex-start;
    gap: 10px;
    line-height: 1.3;
  }
  .contact__icon {
    width: 16px;
    height: 16px;
    flex: none;
    margin-top: 1px;
  }
</style>
</head>
<body>
<main class="canvas">

  <section class="card card--front" aria-label="Card front">
    <span class="brand-dot"></span>
    <span class="brand-name">Shoreline<br>Perks Club</span>
  </section>

  <section class="card card--back" aria-label="Card back">
    <div class="back-top"></div>
    <div class="back-brand">
      <span class="brand-dot"></span>
      <span class="brand-name">Shoreline Perks Club</span>
    </div>

    <div class="contact">
      <p class="contact__name">YOUR NAME HERE</p>
      <p class="contact__title">Solution Manager</p>
      <ul class="contact__list">
        <li class="contact__item">
          <svg class="contact__icon" viewBox="0 0 16 16" fill="#fff"><path d="M4 1h3l1 4-2 1.5a8 8 0 0 0 3.5 3.5L11 8l4 1v3c0 1-1 2-2 2A12 12 0 0 1 2 3c0-1 1-2 2-2z"/></svg>
          <span>123 . 456 78907890</span>
        </li>
        <li class="contact__item">
          <svg class="contact__icon" viewBox="0 0 16 16" fill="#fff"><rect x="4" y="1" width="8" height="4"/><rect x="1" y="6" width="14" height="6" rx="1"/><rect x="4" y="10" width="8" height="5" fill="#3c63c4" stroke="#fff"/></svg>
          <span>123 . 456 78907890</span>
        </li>
        <li class="contact__item">
          <svg class="contact__icon" viewBox="0 0 16 16" fill="none" stroke="#fff" stroke-width="1.5"><rect x="1" y="3" width="14" height="10"/><path d="M1 3l7 6 7-6"/></svg>
          <span>urname@email.com</span>
        </li>
        <li class="contact__item">
          <svg class="contact__icon" viewBox="0 0 16 16" fill="none" stroke="#fff" stroke-width="1.3"><circle cx="8" cy="8" r="6.5"/><ellipse cx="8" cy="8" rx="3" ry="6.5"/><path d="M1.5 8h13"/></svg>
          <span>urwebsitename.com</span>
        </li>
        <li class="contact__item">
          <svg class="contact__icon" viewBox="0 0 16 16" fill="#fff"><path d="M8 0a5.5 5.5 0 0 0-5.5 5.5C2.5 10 8 16 8 16s5.5-6 5.5-10.5A5.5 5.5 0 0 0 8 0zm0 8a2.5 2.5 0 1 1 0-5 2.5 2.5 0 0 1 0 5z"/></svg>
          <span>Street Address Here<br>Bayview City, 2222</span>
        </li>
      </ul>
    </div>
  </section>

</main>
</body>
</html>
```